Rebrand of an existing product label

We are looking for a new design / label for our body lotion. Attached is the current product label. We have this product available in Retinol, Collagen, Hyaluronic Acid, Vitamin C, and Coconut. The brand should reflect a clinical, trustworthy look. We also want to include on the label that the product contains Dead Sea Minerals. Attached is the dieline for the label for the jar and the top. This jar is the packaging that needs to be used for this project.
Updates

Target Market(s)

40+

Requirements
Must have
• Ingredient callouts on the front + benefits. Ex- Vitamin C Brightening Cream

```html
<!DOCTYPE html>
<html lang="en">
<head>
<meta charset="utf-8">
<title>Marina Skin – Cream Jar Labels</title>
<link href="https://fonts.googleapis.com/css2?family=Montserrat:wght@300;400;500;700&display=swap" rel="stylesheet">
<style>
  :root {
    --paper: #ffffff;
    --ink: #1a1a1a;
    --label-edge: #e3e3e3;
    --vitamin: #f39a21;
    --retinol: #7d5aa6;
    --collagen: #e688b7;
  }
  html, body {
    margin: 0;
    padding: 0;
    width: 1200px;
    height: 692px;
    overflow: hidden;
    background: var(--paper);
    font-family: "Montserrat", Arial, sans-serif;
  }
  .canvas { position: relative; width: 1200px; height: 692px; }

  .jar-label {
    position: absolute;
    top: 182px;
    width: 287px;
    height: 191px;
    background: var(--paper);
    border: 1px solid var(--label-edge);
    box-sizing: border-box;
    text-align: center;
    color: var(--ink);
  }
  .jar-label--vitamin { left: 103px; --accent: var(--vitamin); }
  .jar-label--retinol { left: 455px; --accent: var(--retinol); }
  .jar-label--collagen { left: 806px; --accent: var(--collagen); }

  .brand {
    position: absolute;
    top: 22px;
    left: 0; right: 0;
    font-size: 20px;
    font-weight: 400;
    letter-spacing: 0.5px;
    line-height: 24px;
    color: var(--ink);
  }
  .brand-dot {
    display: inline-block;
    width: 12px; height: 12px;
    border: 1.5px solid var(--ink);
    border-radius: 50%;
    margin: 0 6px;
    vertical-align: 1px;
  }
  .ingredient-band {
    position: absolute;
    top: 61px;
    left: -1px; right: -1px;
    height: 54px;
    background: var(--accent);
    color: var(--paper);
  }
  .ingredient-name {
    display: block;
    margin-top: 3px;
    font-size: 33px;
    font-weight: 300;
    line-height: 36px;
    letter-spacing: 0.5px;
  }
  .benefit {
    display: block;
    font-size: 12px;
    font-weight: 300;
    line-height: 14px;
    letter-spacing: 0.3px;
  }
  .usage {
    position: absolute;
    top: 124px;
    left: 0; right: 0;
    font-size: 10.5px;
    font-weight: 400;
    line-height: 13px;
  }
  .minerals {
    position: absolute;
    top: 139px;
    left: 54px;
    width: 179px;
    padding: 2px 0;
    border-top: 1px solid var(--accent);
    border-bottom: 1px solid var(--accent);
    font-size: 8px;
    font-weight: 700;
    line-height: 9px;
    letter-spacing: 0.3px;
  }
  .volume {
    position: absolute;
    top: 158px;
    left: 0; right: 0;
    font-size: 10.5px;
    font-weight: 300;
    line-height: 13px;
  }

  .lid-label {
    position: absolute;
    top: 491px;
    width: 215px;
    height: 142px;
    overflow: visible;
  }
  .lid-label--vitamin { left: 139px; }
  .lid-label--retinol { left: 491px; }
  .lid-label--collagen { left: 842px; }
  .lid-shape-vitamin { fill: var(--vitamin); }
  .lid-shape-retinol { fill: var(--retinol); }
  .lid-shape-collagen { fill: var(--collagen); }
  .lid-ring { fill: none; stroke: var(--paper); stroke-width: 1.2; }
  .lid-title { fill: var(--paper); font-family: "Montserrat", Arial, sans-serif; font-size: 22px; font-weight: 300; }
  .lid-benefit { fill: var(--paper); font-family: "Montserrat", Arial, sans-serif; font-size: 6.5px; font-weight: 400; }
  .lid-arc-text { fill: var(--paper); font-family: "Montserrat", Arial, sans-serif; font-size: 7.5px; font-weight: 400; letter-spacing: 2.2px; }
</style>
</head>
<body>
<main class="canvas">

  <section class="jar-label jar-label--vitamin">
    <div class="brand">MARINA<span class="brand-dot"></span>SKIN</div>
    <div class="ingredient-band">
      <span class="ingredient-name">VITAMIN C</span>
      <span class="benefit">BRIGHTENING CREAM</span>
    </div>
    <div class="usage">MOISTURIZING CREAM FACE, NECK &amp; HANDS</div>
    <div class="minerals">INFUSED WITH DEAD SEA MINERALS</div>
    <div class="volume">16.9 FL OZ (500 ML)</div>
  </section>

  <section class="jar-label jar-label--retinol">
    <div class="brand">MARINA<span class="brand-dot"></span>SKIN</div>
    <div class="ingredient-band">
      <span class="ingredient-name">RETINOL</span>
      <span class="benefit">FIRMING CREAM</span>
    </div>
    <div class="usage">MOISTURIZING CREAM FACE, NECK &amp; HANDS</div>
    <div class="minerals">INFUSED WITH DEAD SEA MINERALS</div>
    <div class="volume">16.9 FL OZ (500 ML)</div>
  </section>

  <section class="jar-label jar-label--collagen">
    <div class="brand">MARINA<span class="brand-dot"></span>SKIN</div>
    <div class="ingredient-band">
      <span class="ingredient-name">COLLAGEN</span>
      <span class="benefit">HYDRATING CREAM</span>
    </div>
    <div class="usage">MOISTURIZING CREAM FACE, NECK &amp; HANDS</div>
    <div class="minerals">INFUSED WITH DEAD SEA MINERALS</div>
    <div class="volume">16.9 FL OZ (500 ML)</div>
  </section>

  <svg class="lid-label lid-label--vitamin" viewBox="0 0 215 142" aria-label="Vitamin C lid label">
    <defs>
      <path id="arc-vitamin" d="M26,52 A81.5,81.5 0 0 0 189,52"/>
    </defs>
    <path class="lid-shape-vitamin" d="M0,40 C0,15 15,0 35,0 C55,0 63,10 72,20 C85,33 95,38 107.5,38 C120,38 130,33 143,20 C152,10 160,0 180,0 C200,0 215,15 215,40 C215,95 165,142 107.5,142 C50,142 0,95 0,40 Z"/>
    <circle class="lid-ring" cx="107.5" cy="62" r="8"/>
    <text class="lid-title" x="107.5" y="96" text-anchor="middle">VITAMIN C</text>
    <text class="lid-benefit" x="107.5" y="106" text-anchor="middle">BRIGHTENING CREAM</text>
    <text class="lid-arc-text"><textPath href="#arc-vitamin" startOffset="50%" text-anchor="middle">MOISTURIZING CREAM FACE, NECK &amp; HANDS</textPath></text>
  </svg>

  <svg class="lid-label lid-label--retinol" viewBox="0 0 215 142" aria-label="Retinol lid label">
    <defs>
      <path id="arc-retinol" d="M26,52 A81.5,81.5 0 0 0 189,52"/>
    </defs>
    <path class="lid-shape-retinol" d="M0,40 C0,15 15,0 35,0 C55,0 63,10 72,20 C85,33 95,38 107.5,38 C120,38 130,33 143,20 C152,10 160,0 180,0 C200,0 215,15 215,40 C215,95 165,142 107.5,142 C50,142 0,95 0,40 Z"/>
    <circle class="lid-ring" cx="107.5" cy="62" r="8"/>
    <text class="lid-title" x="107.5" y="96" text-anchor="middle">RETINOL</text>
    <text class="lid-benefit" x="107.5" y="106" text-anchor="middle">FIRMING CREAM</text>
    <text class="lid-arc-text"><textPath href="#arc-retinol" startOffset="50%" text-anchor="middle">MOISTURIZING CREAM FACE, NECK &amp; HANDS</textPath></text>
  </svg>

  <svg class="lid-label lid-label--collagen" viewBox="0 0 215 142" aria-label="Collagen lid label">
    <defs>
      <path id="arc-collagen" d="M26,52 A81.5,81.5 0 0 0 189,52"/>
    </defs>
    <path class="lid-shape-collagen" d="M0,40 C0,15 15,0 35,0 C55,0 63,10 72,20 C85,33 95,38 107.5,38 C120,38 130,33 143,20 C152,10 160,0 180,0 C200,0 215,15 215,40 C215,95 165,142 107.5,142 C50,142 0,95 0,40 Z"/>
    <circle class="lid-ring" cx="107.5" cy="62" r="8"/>
    <text class="lid-title" x="107.5" y="96" text-anchor="middle">COLLAGEN</text>
    <text class="lid-benefit" x="107.5" y="106" text-anchor="middle">HYDRATING CREAM</text>
    <text class="lid-arc-text"><textPath href="#arc-collagen" startOffset="50%" text-anchor="middle">MOISTURIZING CREAM FACE, NECK &amp; HANDS</textPath></text>
  </svg>

</main>
</body>
</html>
```